Serenity Prayer Art/Poster Design for Canvas Printing

I have been tasked with creating a piece of art containing the complete serenity prayer for a rehab in New York. The final design will essentially be split into 3 sections and printed on 3 canvases which will hang together (please see below for detailed final product requirements).

We are looking for something that has a classic feel to it, but itsn't overly flourish-y or cheezy as many "church-y" things can feel. Fonts similar to that used in the uploaded file are probably the safest but we don't want to inhibit what you would come up with creatively on your own. I am looking for some sort of background behind the words. This can be a picture, ambiance (sort of like in the attached file). It should be beautiful, refreshing and stunning to look at.

Please feel free to use any Harbor Fellowship symbols or colors (feel free to google, "The Harbor Fellowship Flag" "The Harbor Fellowship Crest" "The Harbor Fellowship Shield") in an abstract way in the background. I would not be looking for any literal or exact Fellowship symbols to appear, but using shadows, outlines, etc. is completely acceptable. I'm attaching some CD art which uses The Harbor Fellowship shield in the way I am describing. The words "The Harbor Fellowship" are removed and it is the outline of the shield used in a very modern, simplistic way. Red, Yellow and Blue would be the colors to use ideally as these are the colors of The Harbor Fellowship... you could even get creative and use a different color on each panel.

In the file you will find the complete Serenity prayer. The only words we want on the artwork is:

"God grant me the serenity to accept the things I cannot change; courage to change the things I can; and wisdom to know the difference. Living one day at a time; Enjoying one moment at a time; Accepting hardships as the pathway to peace; Taking, as He did, this sinful world as it is, not as I would have it; Trusting that He will make all things right if I surrender to His Will; That I may be reasonably happy in this life and supremely happy with Him forever in the next. Amen.

- Lambert Osgoodson
Commissioned by Majors Daniel & Fern Oakes"

Please do not italicize the font as it is in the reference.

We are printing the 3 sections on canvases sized 24"w x 48"h. Since there is a folded border that is 1.5" deep, the total size of the artwork should be 75"w x 51"h and we would be expecting 3 files each measuring 27"w x 51"h (to allow room for the border of each canvas while maintaining the integrity of the image as a whole). If there is any confusion as to what we are looking for in terms of dimensions or images, please let me know. It's much simpler than it seems.

I am attaching a VERY rough doodle of the layout to help with any questions.

We want something that is beautiful and inspiring and can't wait to see what you work on!

Target Market(s)

Will be used as hanging art in a rehab center.

Industry/Entity Type

Printing

Font styles to use
Other font styles liked:
• Can be a nice, modern Script font or somethings like Sans Serif.

Colors
0555a3
ec1f27
fbed22
85acd3
f59296
fbf289

Requirements
Must have
• The Serenity Prayer as noted in the notes.
Nice to have
• Modern, abstract use of a Harbor Fellowship symbol in the background somehow.

```html
<!DOCTYPE html>
<html lang="en">
<head>
<meta charset="utf-8">
<title>Serenity Prayer Triptych</title>
<link href="https://fonts.googleapis.com/css2?family=Alegreya+Sans:wght@400;500&display=swap" rel="stylesheet">
<style>
  :root {
    --ray-light: #f3d9a6;
    --ray-mid: #e2a15a;
    --ray-deep: #c8662a;
    --edge-dark: #5a2410;
    --ink: #24160a;
    --crest-orange: #f0832a;
    --divider: #111111;
    --frame-line: rgba(255, 255, 255, 0.55);
  }
  * { margin: 0; padding: 0; box-sizing: border-box; }
  html, body { width: 1200px; height: 749px; overflow: hidden; background: #2a1208; }
  .canvas {
    position: relative;
    width: 1200px;
    height: 749px;
    overflow: hidden;
    font-family: "Alegreya Sans", "Gill Sans", sans-serif;
  }
  .backdrop {
    position: absolute;
    inset: 0;
    background:
      radial-gradient(ellipse 60% 55% at 50% 48%, var(--ray-light) 0%, rgba(243,217,166,0.6) 35%, rgba(226,161,90,0) 70%),
      radial-gradient(ellipse 85% 80% at 50% 48%, var(--ray-mid) 0%, var(--ray-deep) 62%, var(--edge-dark) 100%);
  }
  .crest-name {
    position: absolute;
    left: 0;
    right: 0;
    top: 118px;
    text-align: center;
    font-size: 46px;
    font-weight: 500;
    color: var(--crest-orange);
    opacity: 0.8;
  }
  .frame {
    position: absolute;
    inset: 20px;
    border: 1px solid var(--frame-line);
  }
  .panel-divider {
    position: absolute;
    top: 0;
    width: 7px;
    height: 749px;
    background: var(--divider);
  }
  .panel-divider.left { left: 395px; }
  .panel-divider.right { left: 797px; }
  .prayer {
    position: absolute;
    left: 0;
    right: 0;
    top: 168px;
    text-align: center;
    color: var(--ink);
    font-size: 30px;
    line-height: 43.5px;
  }
  .prayer p { white-space: nowrap; }
  .attribution {
    position: absolute;
    left: 0;
    right: 0;
    top: 602px;
    text-align: center;
    color: var(--ink);
    font-size: 30px;
  }
</style>
</head>
<body>
<main class="canvas">
  <div class="backdrop" role="img" aria-label="Warm orange sunburst with grungy parchment texture and darkened edges"></div>
  <div class="crest-name">The Harbor Fellowship</div>

  <section class="prayer">
    <p>God grant me the serenity to accept the things I cannot change;</p>
    <p>Courage to change the things I can; and wisdom to know the difference.</p>
    <p>Living one day at a time; Enjoying one moment at a time;</p>
    <p>Accepting hardships as the pathway to peace;</p>
    <p>Taking, as He did, this sinful world as it is, not as I would have it;</p>
    <p>Trusting that He will make all things right if I surrender to His Will;</p>
    <p>That I may be reasonably happy in this life</p>
    <p>and supremely happy with Him forever in the next.</p>
    <p>Amen.</p>
  </section>
  <p class="attribution">- Lambert Osgoodson</p>

  <div class="frame"></div>
  <div class="panel-divider left"></div>
  <div class="panel-divider right"></div>
</main>
</body>
</html>
```